CRPG is needing business cards, and stationary created.

Pixel Forge created a logo for our business, and now we are wanting business cards, and stationary. I have included two designs of the same logo. Please feel free to use them as you want. The name of the company is Cedar Ridge Property Group LLC, the address is 812 NE Tamber Ln., Suite 9, the city & state is Bend, Oregon, zip code is 97815, Telephone number is 541-237-4190, Fax number is 541-237-8856, the name on the business card is Travis Lundqor CMCA

Industry/Entity Type

Property Management

Contact Information for Business Card

The card needs to look professional. Upscale.

Requirements
Must have
• The colors we are using are on the logo that has been uploaded.

```html
<!DOCTYPE html>
<html lang="en">
<head>
<meta charset="utf-8">
<title>Cedar Ridge Property Group – Business Card</title>
<link href="https://fonts.googleapis.com/css2?family=Montserrat:wght@400;500;600;700;800&display=swap" rel="stylesheet">
<style>
  :root {
    --page-bg: #e9ebee;
    --card-white: #ffffff;
    --card-navy: #3a4656;
    --brand-teal: #1f8a6e;
    --ink-dark: #2f3a47;
    --ink-mid: #4a5563;
    --ink-light: #ffffff;
    --ink-soft: #c9d0d8;
  }
  * { box-sizing: border-box; margin: 0; padding: 0; }
  html, body {
    width: 1200px;
    height: 870px;
    overflow: hidden;
    background: var(--page-bg);
    font-family: "Montserrat", Arial, sans-serif;
  }
  .card-set {
    position: absolute;
    top: 280px;
    left: 40px;
    display: flex;
    gap: 40px;
  }
  .card {
    width: 540px;
    height: 310px;
    border-radius: 18px;
    position: relative;
    overflow: hidden;
    box-shadow: 0 6px 18px rgba(30, 40, 55, 0.18);
  }
  .card-front { background: var(--card-white); padding: 28px 34px; }
  .card-back {
    background: var(--card-navy);
    display: flex;
    align-items: center;
    justify-content: center;
  }
  .brand { display: flex; align-items: center; gap: 10px; }
  .brand-mark {
    width: 30px;
    height: 30px;
    background: var(--ink-dark);
    flex: none;
  }
  .brand-name {
    font-weight: 800;
    font-size: 24px;
    line-height: 1;
    letter-spacing: 0.5px;
    text-transform: uppercase;
    color: var(--brand-teal);
  }
  .brand-sub {
    margin-top: 4px;
    padding-top: 3px;
    border-top: 1px solid var(--ink-mid);
    font-size: 7.5px;
    font-weight: 700;
    letter-spacing: 1px;
    text-transform: uppercase;
    color: var(--ink-dark);
  }
  .brand-tagline {
    margin-top: 3px;
    font-size: 6.5px;
    font-weight: 600;
    letter-spacing: 3px;
    text-transform: uppercase;
    color: var(--ink-mid);
  }
  .card-back .brand { gap: 14px; }
  .card-back .brand-mark { width: 38px; height: 38px; background: var(--ink-soft); }
  .card-back .brand-name { color: var(--ink-light); font-size: 30px; }
  .card-back .brand-sub { color: var(--ink-soft); border-color: var(--ink-soft); font-size: 8.5px; }
  .card-back .brand-tagline { color: var(--ink-soft); font-size: 7.5px; }
  .holder {
    margin-top: 22px;
    border-left: 4px solid var(--brand-teal);
    padding-left: 12px;
  }
  .holder-name {
    font-size: 15px;
    font-weight: 700;
    color: var(--brand-teal);
    text-transform: uppercase;
    letter-spacing: 0.4px;
  }
  .holder-title { font-size: 10px; color: var(--ink-mid); margin-top: 4px; }
  .address {
    margin-top: 14px;
    font-size: 10.5px;
    line-height: 1.5;
    color: var(--ink-dark);
  }
  .contact-list { list-style: none; margin-top: 12px; }
  .contact-list li {
    display: flex;
    align-items: center;
    gap: 8px;
    font-size: 10.5px;
    line-height: 1.75;
    color: var(--ink-dark);
  }
  .contact-list svg { width: 10px; height: 10px; fill: var(--brand-teal); flex: none; }
</style>
</head>
<body>
  <main class="card-set">
    <section class="card card-front">
      <div class="brand">
        <span class="brand-mark"></span>
        <div class="brand-text">
          <div class="brand-name">Cedar Ridge</div>
          <div class="brand-sub">Property Group</div>
          <div class="brand-tagline">Rooted In Service</div>
        </div>
      </div>
      <div class="holder">
        <div class="holder-name">Travis Lundqor</div>
        <div class="holder-title">CMCA</div>
      </div>
      <div class="address">812 NE Tamber Ln., Suite 9<br>Bend, OR 97815</div>
      <ul class="contact-list">
        <li><svg viewBox="0 0 10 10"><path d="M2 0.5 L3.6 2.6 L2.7 3.7 Q3.8 5.9 6.1 7.2 L7.2 6.3 L9.4 7.9 L8.3 9.5 Q3.5 9 0.5 1.7 Z"/></svg>541-237-4190</li>
        <li><svg viewBox="0 0 10 10"><path d="M2 0 H7 V3 H2 Z M0.5 3.5 H9.5 V8 H8 V10 H2 V8 H0.5 Z M3 6.5 V9 H7 V6.5 Z"/></svg>541-237-8856</li>
        <li><svg viewBox="0 0 10 10"><path d="M0.5 2 H9.5 V8.5 H0.5 Z M1.2 2.6 L5 5.6 L8.8 2.6 V3.6 L5 6.6 L1.2 3.6 Z" fill-rule="evenodd"/></svg>info@cedarridgepg.com</li>
        <li><svg viewBox="0 0 10 10"><circle cx="5" cy="5" r="4.5"/></svg>www.cedarridgepg.com</li>
      </ul>
    </section>
    <section class="card card-back">
      <div class="brand">
        <span class="brand-mark"></span>
        <div class="brand-text">
          <div class="brand-name">Cedar Ridge</div>
          <div class="brand-sub">Property Group</div>
          <div class="brand-tagline">Rooted In Service</div>
        </div>
      </div>
    </section>
  </main>
</body>
</html>
```